Kestrel Grooming Co Box Label

I am putting together a kit made up of beard products (oils,balms etc) which i am calling a "Copperline Tonic Crate". I need to make a label for the box which includes my logo (attached) and would like a bearded man on it as well

```html
<!DOCTYPE html>
<html lang="en">
<head>
<meta charset="utf-8">
<title>Kestrel Grooming Co – Copperline Tonic Crate label options</title>
<link rel="stylesheet" href="https://fonts.googleapis.com/css2?family=Alfa+Slab+One&family=Bebas+Neue&family=Montserrat:wght@500;600&display=swap">
<style>
  :root {
    --board: #1a242b;
    --wood-light: #f0dcbc;
    --wood-mid: #e8cda5;
    --wood-warm: #e3c49a;
    --ink: #231a14;
    --beard-dark: #2e1d0e;
    --beard-mid: #3f2815;
    --copper: #a4581c;
    --walnut: #4a2a12;
    --ribbon: #4a3222;
    --ribbon-fold: #6b4a2e;
    --ribbon-edge: #c9a67c;
    --cream: #f3e5cf;
    --caption: #ffffff;
  }
  * { margin: 0; padding: 0; box-sizing: border-box; }
  html, body {
    width: 1200px; height: 1102px; overflow: hidden;
    background: var(--board);
  }
  .board { position: relative; width: 1200px; height: 1102px; }

  .label {
    position: absolute; width: 521px; height: 433px; overflow: hidden;
    background: linear-gradient(160deg, var(--wood-mid) 0%, var(--wood-light) 45%, var(--wood-warm) 100%);
  }
  .label--op1 { left: 66px; top: 44px; }
  .label--op2 { left: 618px; top: 42px; }
  .label--op3 { left: 61px; top: 558px; }
  .label--op4 { left: 619px; top: 558px; }

  .bearded-man {
    position: absolute; border-radius: 46% 46% 40% 40% / 30% 30% 55% 55%;
    background: radial-gradient(ellipse at 50% 35%, var(--beard-mid) 0%, var(--beard-dark) 70%);
  }
  .label--op1 .bearded-man { left: 42px; top: 50px; width: 180px; height: 362px; }
  .label--op2 .bearded-man { left: 298px; top: 26px; width: 200px; height: 390px; }
  .label--op3 .bearded-man { left: 38px; top: 26px; width: 180px; height: 370px; }
  .label--op4 .bearded-man { left: 37px; top: 50px; width: 165px; height: 345px; }

  .brand-name {
    position: absolute; white-space: nowrap;
    font-family: "Bebas Neue", sans-serif; font-weight: 400;
    font-size: 28px; line-height: 1; letter-spacing: 0.01em; color: var(--ink);
  }
  .label--op1 .brand-name { left: 277px; top: 106px; }
  .label--op2 .brand-name { left: 50px; top: 312px; }
  .label--op3 .brand-name { left: 306px; top: 112px; font-size: 26px; }
  .label--op4 .brand-name { left: 286px; top: 108px; font-size: 24px; }

  /* op1 – condensed stack */
  .title-stack {
    position: absolute; left: 277px; top: 182px;
    font-family: "Bebas Neue", sans-serif; font-size: 58px; line-height: 0.94;
    color: var(--ink);
  }
  .product-line {
    position: absolute; left: 282px; top: 350px; width: 176px; height: 28px;
    border-top: 2px solid var(--ink); border-bottom: 2px solid var(--ink);
    display: flex; justify-content: space-between; align-items: center; padding: 0 4px;
    font-family: "Bebas Neue", sans-serif; font-size: 15px; letter-spacing: 0.06em; color: var(--ink);
  }

  /* op2 – slab stack */
  .slab-stack {
    position: absolute; left: 16px; top: 128px;
    font-family: "Alfa Slab One", serif; font-size: 40px; line-height: 1.08;
  }
  .slab-stack .line-1 { color: var(--copper); }
  .slab-stack .line-2 { color: var(--walnut); }
  .slab-stack .line-3 { color: var(--ink); }

  /* op3 – ribbons */
  .ribbons { position: absolute; left: 225px; top: 160px; width: 296px; height: 205px; }
  .ribbon-text {
    position: absolute; font-family: "Bebas Neue", sans-serif; font-size: 42px;
    line-height: 1; color: var(--cream); letter-spacing: 0.04em; white-space: nowrap;
    transform: translateX(-50%);
  }
  .ribbon-text--1 { left: 170px; top: 8px; }
  .ribbon-text--2 { left: 147px; top: 80px; }
  .ribbon-text--3 { left: 122px; top: 152px; }

  /* op4 – framed title */
  .framed-title {
    position: absolute; left: 242px; top: 163px; width: 245px; height: 159px;
    border: 3px solid var(--ink);
    display: flex; flex-direction: column; justify-content: center; align-items: center;
    font-family: "Montserrat", sans-serif; font-weight: 500; font-size: 24px;
    line-height: 1.5; letter-spacing: 0.14em; color: var(--ink);
  }

  .caption {
    position: absolute; transform: translateX(-50%);
    font-family: "Montserrat", sans-serif; font-weight: 600; font-size: 26px;
    letter-spacing: 0.18em; color: var(--caption);
  }
  .caption--op1 { left: 360px; top: 484px; }
  .caption--op2 { left: 872px; top: 486px; }
  .caption--op3 { left: 349px; top: 1018px; }
  .caption--op4 { left: 860px; top: 1020px; }
</style>
</head>
<body>
<main class="board">

  <section class="label label--op1">
    <div class="bearded-man" role="img" aria-label="Silhouette illustration of a bearded man with swept hair and sunglasses"></div>
    <div class="brand-name">Kestrel Grooming Co</div>
    <h1 class="title-stack">Copperline<br>Tonic<br>Crate</h1>
    <div class="product-line"><span>Oils</span><span>Balms</span><span>Shave Soap</span></div>
  </section>
  <div class="caption caption--op1">op1</div>

  <section class="label label--op2">
    <div class="bearded-man" role="img" aria-label="Silhouette illustration of a bearded man with swept hair and sunglasses"></div>
    <h1 class="slab-stack">
      <div class="line-1">Copperline</div>
      <div class="line-2">Tonic</div>
      <div class="line-3">Crate</div>
    </h1>
    <div class="brand-name">Kestrel Grooming Co</div>
  </section>
  <div class="caption caption--op2">op2</div>

  <section class="label label--op3">
    <div class="bearded-man" role="img" aria-label="Silhouette illustration of a bearded man with swept hair and sunglasses"></div>
    <div class="brand-name">Kestrel Grooming Co</div>
    <div class="ribbons">
      <svg width="296" height="205" viewBox="0 0 296 205" aria-hidden="true">
        <polygon class="ribbon-fold" points="50,54 250,54 240,72 40,72" fill="var(--ribbon-fold)"/>
        <polygon class="ribbon-fold" points="28,126 225,126 215,144 18,144" fill="var(--ribbon-fold)"/>
        <polygon points="60,4 292,4 270,28 289,54 50,54" fill="var(--ribbon)" stroke="var(--ribbon-edge)" stroke-width="1.5"/>
        <line x1="80" y1="47" x2="265" y2="47" stroke="var(--cream)" stroke-width="1.5" stroke-dasharray="2 3"/>
        <polygon points="38,76 265,76 252,126 28,126 36,100" fill="var(--ribbon)" stroke="var(--ribbon-edge)" stroke-width="1.5"/>
        <polygon points="14,148 238,148 230,198 6,198 20,172" fill="var(--ribbon)" stroke="var(--ribbon-edge)" stroke-width="1.5"/>
      </svg>
      <span class="ribbon-text ribbon-text--1">Copperline</span>
      <span class="ribbon-text ribbon-text--2">Tonic</span>
      <span class="ribbon-text ribbon-text--3">Crate</span>
    </div>
  </section>
  <div class="caption caption--op3">op3</div>

  <section class="label label--op4">
    <div class="bearded-man" role="img" aria-label="Silhouette illustration of a bearded man with swept hair and sunglasses"></div>
    <div class="brand-name">Kestrel Grooming Co</div>
    <h1 class="framed-title"><span>COPPERLINE</span><span>TONIC</span><span>CRATE</span></h1>
  </section>
  <div class="caption caption--op4">op4</div>

</main>
</body>
</html>
```